Marvantar - Seafood industry professional promoting page

Hi. I´m in the seafood business with a one man company sourcing and exporting frozen seafood. I need to make a one page homepage for Marvantar (from Iceland). The feeling of it should be; Trustworthy, experience and knowledge.
Using as background a picture (or part of it), or a moving video:

http://www1.brelvik.is/sjorinn/myndir/ufsinn.jpg
https://clipvera.com/583720415

Main text to be:

- We can help source, market and add value to your seafood business
- Years of experience in seafood trade and production
- Extensive knowledge of fishing, seasonality, production and accreditations

Contact:
dagur@marvantar.is
Tel: +3654170392
(with a photo)

p.s. please also make logo look better.

Target Market(s)

Seafood industry

Industry/Entity Type

Business

Logo Text

Marvantar

Coding

Coded - Design and coding required

Number of Pages Required

1 page

Colors
0792cd
33a6d7

```html
<!DOCTYPE html>
<html lang="en">
<head>
<meta charset="utf-8">
<title>Marvantar – Sourcing and Exporting Seafood</title>
<link rel="stylesheet" href="https://fonts.googleapis.com/css2?family=Cinzel:wght@700&family=Montserrat:wght@700&family=Lora:wght@400&display=swap">
<style>
:root{
  --navy:#1b3a66;
  --ink:#0f2563;
  --sea-deep:#0b4f66;
  --sea-mid:#14828f;
  --sea-light:#2ab4c9;
  --card-1:#1f5d8e;
  --card-2:#2388b8;
  --card-3:#55abd0;
  --brand:#0792cd;
  --brand-2:#33a6d7;
  --page:#f7f7f7;
  --mist:#e8f0f8;
  --muted:#8a8a8a;
  --accent-red:#d22;
}
*{box-sizing:border-box;margin:0;padding:0}
html,body{width:742px;height:1200px;overflow:hidden}
body{background:var(--page);position:relative;font-family:'Lora',serif;color:#333}
.abs{position:absolute}
.hero-bg{left:0;top:0;width:742px;height:478px;background:radial-gradient(ellipse at 30% 10%,var(--sea-light),transparent 60%),linear-gradient(180deg,#18a3c0 0%,var(--sea-mid) 45%,var(--sea-deep) 100%)}
.nav{left:81px;top:12px;width:576px;height:42px;background:var(--navy);display:flex;align-items:center;padding:0 10px}
.nav-brand{display:flex;align-items:center;gap:6px;color:#fff;font-family:'Montserrat',sans-serif;font-size:13px;font-weight:700}
.nav-brand .mark{width:8px;height:8px;background:#fff}
.nav-divider{width:1px;height:20px;background:#fff;margin:0 10px 0 14px}
.nav-tag{color:#fff;font-family:'Montserrat',sans-serif;font-size:7px;line-height:10px;font-weight:700}
.nav-links{margin-left:auto;display:flex;gap:4px}
.nav-links a{font-family:'Cinzel',serif;font-size:6.5px;color:#fff;text-decoration:none;padding:8px 10px}
.nav-links a.active{background:#2a5a8a;border-radius:2px}
.hero-title{left:103px;top:91px;width:262px;height:112px;background:rgba(10,90,90,.55);color:#fff;font-family:'Cinzel',serif;font-size:19px;line-height:28px;padding:3px 2px}
.btn-more{left:103px;top:211px;width:50px;height:21px;background:#f2f2f2;border-radius:3px;font-size:6.5px;color:var(--ink);display:flex;align-items:center;justify-content:center}
.services{left:81px;top:279px;width:581px;height:191px;display:flex}
.service{flex:1;color:#fff;text-align:center;padding-top:22px;border-bottom:8px solid rgba(255,255,255,.12)}
.service:nth-child(1){background:var(--card-1)}
.service:nth-child(2){background:var(--card-2)}
.service:nth-child(3){background:var(--card-3)}
.service svg{width:38px;height:38px}
.service h3{font-family:'Cinzel',serif;font-size:12px;line-height:16px;margin-top:14px}
.service .dots{font-size:8px;line-height:8px}
.service p{font-size:6px;line-height:10.5px;padding:0 20px;margin-top:4px}
.welcome{left:81px;top:470px;width:581px;height:126px;background:#fff}
.welcome h2{position:absolute;left:0;width:395px;top:22px;text-align:center;font-family:'Cinzel',serif;color:var(--ink);font-size:15px}
.welcome .dots{position:absolute;left:0;width:395px;top:38px;text-align:center;color:var(--accent-red);font-size:10px}
.welcome p{position:absolute;left:25px;width:345px;top:56px;text-align:center;font-size:6.2px;line-height:13.3px;color:var(--muted)}
.logo-box{left:470px;top:489px;width:176px;height:85px;background:#f2f2f2;padding:5px}
.logo-inner{width:100%;height:100%;background:#fff;display:flex;align-items:center;justify-content:center;gap:8px;font-family:'Montserrat',sans-serif;font-weight:700;font-size:22px;color:var(--brand)}
.logo-inner .mark{width:14px;height:14px;background:var(--brand)}
.products-title{left:0;width:742px;top:596px;text-align:center;font-family:'Cinzel',serif;color:var(--ink);font-size:15px}
.product{top:630px;width:127px;height:88px}
.product .photo{height:62px}
.product .label{height:26px;background:var(--card-2);color:#fff;font-size:9.5px;display:flex;align-items:center;justify-content:center}
.strip{left:81px;top:755px;width:581px;height:70px;background:linear-gradient(90deg,#c8d8e4,#e3ecf2 40%,#d4e2ec 70%,#eef3f6)}
.strip .item{position:absolute;top:18px;display:flex;gap:16px;align-items:center}
.strip small{display:block;font-size:5.5px;color:#555}
.strip span{font-size:8.5px;color:#667}
.contact{left:81px;top:825px;width:581px;height:316px;background:var(--mist)}
.contact h2{position:absolute;top:26px;width:100%;text-align:center;font-family:'Cinzel',serif;color:var(--ink);font-size:18px}
.contact .intro{position:absolute;top:64px;left:110px;width:361px;text-align:center;font-size:6px;line-height:10.5px;color:#555}
.field{position:absolute;border:1px solid #d5e0e8;background:#e6eef4;font-size:5.5px;color:#999;padding:4px 5px}
.send{position:absolute;left:257px;top:249px;width:62px;height:17px;background:var(--card-2);border-radius:2px;color:#fff;font-size:5.5px;display:flex;align-items:center;justify-content:center}
.footer{left:81px;top:1141px;width:581px;height:46px;background:var(--card-3);color:#fff;font-size:9px;display:flex;align-items:center;justify-content:center}
</style>
</head>
<body>
<div class="abs hero-bg" role="img" aria-label="Underwater photo of pollock swimming in teal sea"></div>

<header class="abs nav">
  <div class="nav-brand"><span class="mark"></span>Marvantar</div>
  <div class="nav-divider"></div>
  <div class="nav-tag">SOURCING AND<br>EXPORTING SEAFOOD</div>
  <nav class="nav-links"><a class="active">Home</a><a>About Us</a><a>Contact Us</a></nav>
</header>

<h1 class="abs hero-title">We can help source, market and add value to your seafood business</h1>
<div class="abs btn-more">View more</div>

<section class="abs services">
  <div class="service">
    <svg viewBox="0 0 40 40" role="img" aria-label="Sourcing icon"><circle cx="20" cy="20" r="15" fill="none" stroke="#fff" stroke-width="1.5"/></svg>
    <h3>Sourcing<br>Seafood</h3><div class="dots">. . .</div>
    <p>Etiam ullamcorper. Suspendisse a pellentesque dui, non felis. Maecenas malesuada elit lectus felis, malesuada ultricies. Curabitur et ligula. Ut molestie a, ultricies porta.</p>
  </div>
  <div class="service">
    <svg viewBox="0 0 40 40"><circle cx="20" cy="20" r="17" fill="none" stroke="#fff" stroke-width="1.5"/><path d="M9 22h22l-3 5H12z" fill="#fff"/><rect x="16" y="16" width="10" height="5" fill="#fff"/><rect x="13" y="14" width="2" height="7" fill="#fff"/></svg>
    <h3>Exporting<br>Seafood</h3><div class="dots">. . .</div>
    <p>Etiam ullamcorper. Suspendisse a pellentesque dui, non felis. Maecenas malesuada elit lectus felis, malesuada ultricies. Curabitur et ligula. Ut molestie a, ultricies porta.</p>
  </div>
  <div class="service">
    <svg viewBox="0 0 40 40"><rect x="4" y="8" width="32" height="26" rx="1" fill="none" stroke="#fff" stroke-width="1.5"/><rect x="8" y="13" width="9" height="16" fill="none" stroke="#fff" stroke-width="1.3"/><circle cx="12.5" cy="18" r="2.3" fill="#fff"/><path d="M9 27c1-4 6-4 7 0z" fill="#fff"/><path d="M21 17h11M21 22h11M21 27h11" stroke="#fff" stroke-width="1.5"/></svg>
    <h3>Contact<br>Us</h3><div class="dots">. . .</div>
    <p>Etiam ullamcorper. Suspendisse a pellentesque dui, non felis. Maecenas malesuada elit lectus felis, malesuada ultricies. Curabitur et ligula. Ut molestie a, ultricies porta.</p>
  </div>
</section>

<section class="abs welcome">
  <h2>Welcome to Marvantar</h2>
  <div class="dots">. . .</div>
  <p>Ut molestie a, ultricies porta urna. Vestibulum commodo volutpat a, convallis ac, laoreet enim. Phasellus fermentum in, dolor. Pellentesque facilisis. Nulla imperdiet sit amet magna. Vestibulum dapibus, mauris nec malesuada fames ac turpis velit, rhoncus eu, luctus et interdum adipiscing wisi. Aliquam erat ac ipsum. Integer aliquam purus. Quisque lorem tortor fringilla sed, vestibulum id.</p>
</section>
<div class="abs logo-box"><div class="logo-inner"><span class="mark"></span>Marvantar</div></div>

<h2 class="abs products-title">Some Of Our Frozen Seafood</h2>
<div class="abs product" style="left:101px"><div class="photo" role="img" aria-label="Photo of frozen cod" style="background:linear-gradient(#c9c9c9,#6f6a66)"></div><div class="label">FROZEN COD</div></div>
<div class="abs product" style="left:238px"><div class="photo" role="img" aria-label="Photo of frozen catfish" style="background:linear-gradient(#8a8f95,#cfd3d8)"></div><div class="label">FROZEN CATFISH</div></div>
<div class="abs product" style="left:376px"><div class="photo" role="img" aria-label="Photo of frozen lobster" style="background:linear-gradient(#c4503a,#8e2d22)"></div><div class="label">FROZEN LOBSTER</div></div>
<div class="abs product" style="left:514px"><div class="photo" role="img" aria-label="Photo of frozen crab" style="background:linear-gradient(#b8b4b0,#76716c)"></div><div class="label">FROZEN CRAB</div></div>

<section class="abs strip" role="img" aria-label="Faint snowy mountain backdrop">
  <div class="item" style="left:22px">
    <svg width="24" height="16" viewBox="0 0 24 16"><rect x="1" y="1" width="22" height="14" fill="none" stroke="#2a8bb5" stroke-width="1.3"/><path d="M1 1l11 8 11-8M1 15l8-7M23 15l-8-7" fill="none" stroke="#2a8bb5" stroke-width="1.3"/></svg>
    <div><small>Have any questions?</small><span>NOREPLY@MARVANTAR.COM</span></div>
  </div>
  <div class="item" style="left:302px">
    <svg width="24" height="22" viewBox="0 0 24 22"><path d="M12 2C6 2 2 5.5 2 10c0 3 2 5 4 6l-2 5 6-4c1 .3 1.5.3 2 .3 6 0 10-3.5 10-7.5S18 2 12 2z" fill="none" stroke="#2a8bb5" stroke-width="1.3"/></svg>
    <div><small>Call us</small><span>+61 (0) 3 5521 0947</span></div>
  </div>
</section>

<section class="abs contact">
  <h2>Send us a message</h2>
  <p class="intro">Lorem ipsum dolor sit amet, consectetur adipisicing elit, sed do eiusmod tempor incididunt ut labore et dolore magna alm accusantium doloremque laudantium, totam rem aperiam, eaque ipsequi nesciunt.</p>
  <div class="field" style="left:112px;top:112px;width:175px;height:17px">Your name</div>
  <div class="field" style="left:293px;top:112px;width:176px;height:17px">Your e-mail</div>
  <div class="field" style="left:112px;top:134px;width:357px;height:17px">Subject</div>
  <div class="field" style="left:112px;top:157px;width:357px;height:87px">Message</div>
  <div class="send">Send A Message</div>
</section>

<footer class="abs footer">© 2018 MARVANTAR SEAFOOD</footer>
</body>
</html>
```